TriVex Business Card Design - double sided -plumbing local plumbing company

We have a Plumbing company where the design was create through Sketch Hive. We would now like a business card designed as well. We want it to be in the colour version of the logo.

Details below for the card.

Phone Number: 0438 615 247
Email: info@trivexplumbing.example.au
Website: https://trivexplumbing.example.au
We really want a sophisticated design that stand out from the other- informative and timeless.

Target Market(s)

local Canberra market

Industry/Entity Type

Plumbing, gas fitting, hot water

Contact Information for Business Card

Phone number, email, logo and "Supplying all your heating, cooling and hot water needs"

Requirements
Must have
• bust be colourful, must also be though about it being printed on a magnet. must Vex with the logo - I dont want the logo and information chucked onto a white canvas I would prefer it to be smooth and look purposeful

```html
<!DOCTYPE html>
<html lang="en">
<head>
<meta charset="utf-8">
<title>TriVex Business Card</title>
<link href="https://fonts.googleapis.com/css2?family=Jost:wght@300;400;700&display=swap" rel="stylesheet">
<style>
  :root {
    --page-bg: #ffffff;
    --card-deep: #0a5592;
    --card-mid: #0760a8;
    --card-light: #0d6cb8;
    --brand-sky: #19a7e8;
    --ink-white: #ffffff;
    --icon-ink: #0a5a9c;
  }
  * { margin: 0; padding: 0; box-sizing: border-box; }
  html, body {
    width: 1200px;
    height: 1200px;
    overflow: hidden;
    background: var(--page-bg);
    font-family: "Jost", "Futura", sans-serif;
  }
  .sheet {
    position: relative;
    width: 1200px;
    height: 1200px;
  }
  .card {
    position: absolute;
    left: 243px;
    width: 714px;
    height: 408px;
    overflow: hidden;
  }
  .card-front { top: 164px; }
  .card-back { top: 628px; }
  .card-texture {
    position: absolute;
    inset: 0;
    background:
      linear-gradient(45deg, var(--card-light) 0%, var(--card-mid) 40%, var(--card-deep) 100%);
  }
  .front-content {
    position: absolute;
    inset: 0;
    display: flex;
    flex-direction: column;
    align-items: center;
    padding-top: 142px;
  }
  .brand-name {
    font-weight: 700;
    font-size: 88px;
    line-height: 1;
    letter-spacing: 2px;
    color: var(--brand-sky);
    text-transform: uppercase;
  }
  .tagline {
    margin-top: 22px;
    font-weight: 700;
    font-size: 8px;
    letter-spacing: 2.2px;
    color: var(--ink-white);
    text-transform: uppercase;
  }
  .contact-list {
    position: absolute;
    left: 96px;
    top: 150px;
    list-style: none;
  }
  .contact-item {
    display: flex;
    align-items: center;
    height: 40px;
    margin-bottom: 39px;
  }
  .contact-icon {
    width: 40px;
    height: 40px;
    border-radius: 4px;
    background: var(--ink-white);
    display: flex;
    align-items: center;
    justify-content: center;
    margin-right: 34px;
    flex-shrink: 0;
  }
  .contact-text {
    color: var(--ink-white);
    font-weight: 300;
  }
  .contact-phone { font-size: 25px; }
  .contact-email { font-size: 32px; }
</style>
</head>
<body>
<main class="sheet">
  <section class="card card-front" aria-label="Business card front">
    <div class="card-texture" role="img" aria-label="Blue background with a soft diamond tile pattern"></div>
    <div class="front-content">
      <h1 class="brand-name">TriVex</h1>
      <p class="tagline">Supplying all your heating, cooling and hot water needs</p>
    </div>
  </section>

  <section class="card card-back" aria-label="Business card back">
    <div class="card-texture" role="img" aria-label="Blue background with a soft diamond tile pattern"></div>
    <ul class="contact-list">
      <li class="contact-item">
        <span class="contact-icon">
          <svg width="24" height="24" viewBox="0 0 24 24" aria-hidden="true">
            <path fill="var(--icon-ink)" d="M6.6 10.8a15.2 15.2 0 0 0 6.6 6.6l2.2-2.2c.3-.3.7-.4 1-.2 1.1.4 2.3.6 3.6.6.6 0 1 .4 1 1V20c0 .6-.4 1-1 1A17 17 0 0 1 3 4c0-.6.4-1 1-1h3.5c.6 0 1 .4 1 1 0 1.3.2 2.5.6 3.6.1.3 0 .7-.2 1l-2.3 2.2z"/>
          </svg>
        </span>
        <span class="contact-text contact-phone">0438 615 247</span>
      </li>
      <li class="contact-item">
        <span class="contact-icon">
          <svg width="26" height="20" viewBox="0 0 26 20" aria-hidden="true">
            <rect x="1" y="1.5" width="24" height="17" fill="none" stroke="var(--icon-ink)" stroke-width="1.6"/>
            <path d="M1 1.5l12 9.5 12-9.5M1 18.5l9-7.5M25 18.5l-9-7.5" fill="none" stroke="var(--icon-ink)" stroke-width="1.4"/>
          </svg>
        </span>
        <span class="contact-text contact-email">info@trivexplumbing.example.au</span>
      </li>
    </ul>
  </section>
</main>
</body>
</html>
```